Notepads for Marketing pieces-BOLD design

Looking for notepads for marketing pieces with logo, phone number, and website. Maybe something faded in background. Looking for bold and different

```html
<!DOCTYPE html>
<html lang="en">
<head>
<meta charset="utf-8">
<title>VitalWay Notepad Options</title>
<link href="https://fonts.googleapis.com/css2?family=Montserrat:wght@500&family=Ubuntu:wght@500;700&display=swap" rel="stylesheet">
<style>
  :root {
    --stage: #b3b3b3;
    --paper: #ffffff;
    --red: #f20000;
    --black: #0d0d0d;
    --ink: #1a1a1a;
    --rule: #e2e2e2;
    --faint: rgba(240, 0, 0, 0.06);
    --faint-text: #ececec;
  }
  * { box-sizing: border-box; margin: 0; padding: 0; }
  html, body { width: 1200px; height: 568px; overflow: hidden; }
  body { background: var(--stage); position: relative; font-family: "Ubuntu", sans-serif; color: var(--ink); }

  .option-label {
    position: absolute; top: 27px;
    font-family: "Montserrat", sans-serif; font-weight: 500;
    font-size: 17px; letter-spacing: 2px; color: #fff;
  }
  .sheet {
    position: absolute; top: 58px; width: 336px; height: 481px;
    background: var(--paper); overflow: hidden;
  }
  .sheet-1 { left: 49px; }
  .sheet-2 { left: 423px; }
  .sheet-3 { left: 799px; }

  .deco { position: absolute; inset: 0; width: 336px; height: 481px; }

  .ruled-area {
    position: absolute; left: 23px; width: 294px; top: 113px; height: 300px;
    background: repeating-linear-gradient(to bottom, var(--rule) 0 1px, transparent 1px 14.2px);
  }
  .faint-block {
    position: absolute; left: 230px; top: 119px; width: 87px; height: 285px;
    background: var(--faint);
  }

  .brand-name {
    position: absolute; left: 0; right: 0; text-align: center;
    font-family: "Ubuntu", sans-serif; font-weight: 700; color: var(--red);
    letter-spacing: 1.5px; line-height: 1;
  }
  .tagline {
    position: absolute; left: 0; right: 0; text-align: center;
    font-weight: 500; white-space: nowrap; line-height: 1;
  }
  .tagline .sep { color: var(--red); padding: 0 2px; }

  .contact {
    position: absolute; display: flex; align-items: center; gap: 5px;
    font-weight: 500; white-space: nowrap; line-height: 1;
  }
  .contact svg { flex: none; }
  .on-dark { color: #fff; }

  .sheet-1 .brand-name, .sheet-3 .brand-name { top: 52px; font-size: 31px; }
  .sheet-1 .tagline, .sheet-3 .tagline { top: 89px; font-size: 7.4px; }

  .sheet-2 .brand-name.head { top: 35px; font-size: 20px; }
  .sheet-2 .tagline { top: 61px; font-size: 5px; }
  .sheet-2 .contact { top: 74px; font-size: 8px; }
  .sheet-2 .watermark-name {
    top: 434px; font-size: 56px; color: var(--faint-text); letter-spacing: 2px;
  }

  .footer-contact { font-size: 8.4px; }
  .footer-brand {
    position: absolute; left: 241px; top: 458px; font-size: 13.5px;
    font-weight: 700; color: var(--red); letter-spacing: 0.5px; line-height: 1;
  }
</style>
</head>
<body>

<div class="option-label" style="left:300px">OPTION 1</div>
<div class="option-label" style="left:673px">OPTION 2</div>
<div class="option-label" style="left:1047px">OPTION 3</div>

<!-- Option 1 -->
<section class="sheet sheet-1">
  <div class="faint-block" aria-hidden="true"></div>
  <div class="ruled-area"></div>
  <svg class="deco" viewBox="0 0 336 481" aria-hidden="true">
    <polygon points="0,0 58,0 0,80" fill="var(--red)"/>
    <polygon points="62,0 78,0 0,99 0,86" fill="var(--black)"/>
    <polyline points="0,426 211,426 215,410 220,436 224,421 228,426 336,426" fill="none" stroke="var(--red)" stroke-width="1.6"/>
    <polygon points="0,430 271,430 228,481 0,481" fill="var(--black)"/>
    <polygon points="273,430 336,430 336,481 231,481" fill="var(--red)"/>
    <g transform="translate(296,454)" fill="none" stroke="#fff" stroke-width="2.2" stroke-linejoin="round">
      <polyline points="-12,-1 0,-11 12,-1"/>
      <rect x="-9" y="-2" width="18" height="13" fill="#fff" stroke="none"/>
      <path d="M0 0v9M-4.5 4.5h9" stroke="var(--red)" stroke-width="2.6"/>
    </g>
  </svg>
  <div class="brand-name">VITALWAY</div>
  <div class="tagline">Home Health<span class="sep">|</span>Medical Staffing<span class="sep">|</span>Outpatient Therapy</div>
  <div class="contact footer-contact on-dark" style="left:24px;top:449px">
    <svg width="14" height="14" viewBox="0 0 14 14"><circle cx="7" cy="7" r="7" fill="var(--red)"/><path d="M4.3 3.6l1.4-.4.9 2-1 .8c.4 1 1.2 1.8 2.2 2.2l.8-1 2 .9-.4 1.4c-3.3.2-6.1-2.6-5.9-5.9z" fill="#fff"/></svg>
    555-218-4630
  </div>
  <div class="contact footer-contact on-dark" style="left:119px;top:449px">
    <svg width="14" height="14" viewBox="0 0 14 14"><circle cx="7" cy="7" r="7" fill="var(--red)"/><g fill="none" stroke="#fff" stroke-width="0.9"><circle cx="7" cy="7" r="3.8"/><ellipse cx="7" cy="7" rx="1.7" ry="3.8"/><path d="M3.2 7h7.6"/></g></svg>
    www.vitalwaycare.com
  </div>
</section>

<!-- Option 2 -->
<section class="sheet sheet-2">
  <div class="ruled-area" style="left:24px;width:296px;"></div>
  <div class="brand-name watermark-name" aria-hidden="true">VITALWAY</div>
  <div class="brand-name head">VITALWAY</div>
  <div class="tagline">Home Health<span class="sep">|</span>Medical Staffing<span class="sep">|</span>Outpatient Therapy</div>
  <div class="contact" style="left:82px">
    <svg width="15" height="15" viewBox="0 0 14 14"><circle cx="7" cy="7" r="7" fill="var(--red)"/><path d="M4.3 3.6l1.4-.4.9 2-1 .8c.4 1 1.2 1.8 2.2 2.2l.8-1 2 .9-.4 1.4c-3.3.2-6.1-2.6-5.9-5.9z" fill="#fff"/></svg>
    555-218-4630
  </div>
  <div class="contact" style="left:173px">
    <svg width="15" height="15" viewBox="0 0 14 14"><circle cx="7" cy="7" r="7" fill="var(--red)"/><g fill="none" stroke="#fff" stroke-width="0.9"><circle cx="7" cy="7" r="3.8"/><ellipse cx="7" cy="7" rx="1.7" ry="3.8"/><path d="M3.2 7h7.6"/></g></svg>
    www.vitalwaycare.com
  </div>
</section>

<!-- Option 3 -->
<section class="sheet sheet-3">
  <div class="faint-block" aria-hidden="true"></div>
  <div class="ruled-area"></div>
  <svg class="deco" viewBox="0 0 336 481" aria-hidden="true">
    <polygon points="0,0 58,0 0,80" fill="var(--red)"/>
    <polygon points="62,0 78,0 0,99 0,86" fill="var(--black)"/>
    <polyline points="0,443 224,443 228,427 233,452 237,437 241,443 336,443" fill="none" stroke="var(--red)" stroke-width="2"/>
    <rect x="0" y="448" width="336" height="33" fill="var(--black)"/>
  </svg>
  <div class="brand-name">VITALWAY</div>
  <div class="tagline">Home Health<span class="sep">|</span>Medical Staffing<span class="sep">|</span>Outpatient Therapy</div>
  <div class="contact footer-contact on-dark" style="left:24px;top:458px">
    <svg width="14" height="14" viewBox="0 0 14 14"><circle cx="7" cy="7" r="7" fill="var(--red)"/><path d="M4.3 3.6l1.4-.4.9 2-1 .8c.4 1 1.2 1.8 2.2 2.2l.8-1 2 .9-.4 1.4c-3.3.2-6.1-2.6-5.9-5.9z" fill="#fff"/></svg>
    555-218-4630
  </div>
  <div class="contact footer-contact on-dark" style="left:119px;top:458px">
    <svg width="14" height="14" viewBox="0 0 14 14"><circle cx="7" cy="7" r="7" fill="var(--red)"/><g fill="none" stroke="#fff" stroke-width="0.9"><circle cx="7" cy="7" r="3.8"/><ellipse cx="7" cy="7" rx="1.7" ry="3.8"/><path d="M3.2 7h7.6"/></g></svg>
    www.vitalwaycare.com
  </div>
  <div class="footer-brand">VITALWAY</div>
</section>

</body>
</html>
```